The Morrow Ledgers Website

I need a website to help promote the series of science fiction novels that I am in the process of writing.

I have some content and photos and am in the process of getting some new book cover artwork designed.

I have a current website/domain etc http://www.vantorpagehouse.co.nz but I need something a little more professional and eye catchig but I also want to be able to manage the content myself.

I can send e-versions of the two completed novels for context to any takers

```html
<!DOCTYPE html>
<html lang="en">
<head>
<meta charset="utf-8">
<title>The Morrow Ledgers</title>
<link rel="stylesheet" href="https://fonts.googleapis.com/css2?family=Gelasio:wght@400;500&display=swap">
<style>
:root{
  --page:#f5f5f5;
  --ink:#333333;
  --ink-soft:#555555;
  --accent:#e00000;
  --dark:#262626;
  --white:#ffffff;
  --chirp:#3fbfd1;
  --folio:#3b5998;
}
*{margin:0;padding:0;box-sizing:border-box}
html,body{width:1085px;height:1200px;overflow:hidden}
body{background:var(--page);font-family:"Gelasio",Georgia,serif;color:var(--ink);position:relative}
.abs{position:absolute}
.site-title{left:150px;top:22px;font-size:27px;font-weight:400;color:#111}
.site-title span{color:var(--accent)}
.main-nav{left:150px;top:64px;width:784px;height:56px;background:var(--dark)}
.main-nav a{position:absolute;top:18px;font-size:15px;color:var(--white);text-decoration:none}
.main-nav a.current{color:var(--accent)}
.search{position:absolute;left:605px;top:18px;width:167px;height:21px;background:var(--white);border:1px solid #ccc;border-radius:2px;font-size:11px;color:#aaa;padding:3px 4px}
.search svg{position:absolute;right:5px;top:5px}
.hero{left:150px;top:120px;width:784px;height:335px;background:linear-gradient(135deg,#5a5560 0%,#2d2a38 35%,#8a6a4a 60%,#3a3d55 85%,#b9b6b4 100%)}
.dots{left:505px;top:423px;display:flex;gap:7px}
.dots i{width:13px;height:13px;border-radius:50%;background:var(--white)}
.dots i.on{background:var(--accent)}
.welcome{left:150px;top:477px;width:784px;text-align:center}
.welcome h1{font-size:22px;font-weight:400;color:var(--accent);margin-bottom:9px}
.welcome p{font-size:11.2px;line-height:20px;color:var(--ink-soft);white-space:nowrap}
.col h2{font-size:15px;font-weight:400;color:var(--accent);white-space:nowrap}
.cover{width:87px;height:138px}
.cover-second{background:linear-gradient(180deg,#c81e1e 0 20%,#1a1a1a 20% 70%,#e30000 70%)}
.cover-first{background:linear-gradient(180deg,#1a1a1a 0 8%,#9a9a9a 8% 68%,#f2f2f2 68% 96%,#1a1a1a 96%)}
.col h3{font-size:11.3px;font-weight:500;color:var(--accent)}
.col p{font-size:11.3px;line-height:20px;color:var(--ink)}
.btn{width:80px;height:32px;background:var(--accent);color:var(--white);font-size:11.3px;line-height:32px;text-align:center}
.gallery-main{left:684px;top:656px;width:250px;height:214px;background:radial-gradient(ellipse at 50% 55%,#6e6055 0%,#3a3633 45%,#1c1c1c 100%)}
.gallery-main svg{position:absolute;top:93px}
.thumb{top:888px;width:80px;height:58px}
.t1{left:684px;background:linear-gradient(135deg,#7a2a1a,#b06a4a 50%,#3a1a14)}
.t2{left:769px;background:linear-gradient(135deg,#c2a18a,#8a4a3a 50%,#d8c9bb)}
.t3{left:854px;background:linear-gradient(135deg,#5a3a3a,#c04a5a 50%,#3a2a2a)}
.gallery-text{left:684px;top:949px;width:250px;font-size:11.3px;line-height:20px;color:var(--ink-soft)}
.footer{left:0;top:1097px;width:1085px;height:103px;background:var(--dark)}
.footer-nav{position:absolute;left:176px;top:30px;font-size:15px;color:var(--white);white-space:nowrap}
.footer-nav span{margin:0 11px}
.copyright{position:absolute;left:180px;top:60px;font-size:15px;color:var(--white)}
.social{position:absolute;top:39px;width:44px;height:44px;border-radius:50%;color:var(--white);font-size:10px;line-height:44px;text-align:center}
.social.chirp{left:842px;background:var(--chirp)}
.social.folio{left:891px;background:var(--folio)}
</style>
</head>
<body>
<div class="abs site-title">The <span>Morrow</span> Ledgers</div>

<nav class="abs main-nav">
  <a class="current" style="left:27px">Home</a>
  <a style="left:85px">Reviews</a>
  <a style="left:150px">About</a>
  <a style="left:205px">Blog</a>
  <a style="left:253px">Contact</a>
  <a style="left:319px">Links</a>
  <div class="search">Search
    <svg width="9" height="9" viewBox="0 0 9 9"><circle cx="3.5" cy="3.5" r="2.5" fill="none" stroke="#aaa" stroke-width="1"/><line x1="5.3" y1="5.3" x2="8" y2="8" stroke="#aaa" stroke-width="1.2"/></svg>
  </div>
</nav>

<div class="abs hero" role="img" aria-label="Photo of a table display stacked with science fiction paperbacks"></div>
<div class="abs dots"><i class="on"></i><i></i><i></i><i></i></div>

<section class="abs welcome">
  <h1>Welcome to The Morrow Ledgers</h1>
  <p>The Morrow Ledgers come to Callum's scifi page where you can find links to his scifi novels: Morrow - The First Ledger and the recently published The<br>Hollow Return.Morrow is the first novel in the Morrow series and the Hollow Return is part two of &nbsp;the trilogy.<br>This site is all about unashamed self promotion of Callum's novels</p>
</section>

<section class="col">
  <h2 class="abs" style="left:151px;top:618px">Book Launch Of The Hollow Return</h2>
  <div class="abs cover cover-second" style="left:150px;top:657px" role="img" aria-label="Cover art for The Hollow Return"></div>
  <h3 class="abs" style="left:150px;top:814px">The Hollow Return</h3>
  <p class="abs" style="left:150px;top:852px;width:245px">Welcome to Morrow – the most technically sophisticated and powerful civilization in the known universe.<br>The Hollow Return is the second novel in the Morrow Ledgers series and follows on from the first novel where our unlikely protagonists were kidnapped by a desperate food research team from the Planet Morrow.</p>
  <div class="abs btn" style="left:150px;top:1034px">Read More</div>
</section>

<section class="col">
  <h2 class="abs" style="left:421px;top:618px">The First Ledger</h2>
  <div class="abs cover cover-first" style="left:418px;top:656px" role="img" aria-label="Cover art for The First Ledger"></div>
  <h3 class="abs" style="left:421px;top:814px">The First Ledger</h3>
  <p class="abs" style="left:421px;top:852px;width:255px">Morrow is an imaginative science fiction novel of considerable skill that pokes fun at all forms of political correctness, while also indicating there are dangerous signs of a disintegrating world that is not adequately taken care of. Readers will recognise these as parallels to life on earth. readers to laugh at their own attitudes.</p>
  <div class="abs btn" style="left:419px;top:1034px">Read More</div>
</section>

<section class="col">
  <h2 class="abs" style="left:684px;top:618px">Gallery</h2>
  <div class="abs gallery-main" role="img" aria-label="Gallery photo of a costumed alien figure at a book display">
    <svg style="left:18px" width="20" height="30" viewBox="0 0 20 30"><polyline points="16,2 4,15 16,28" fill="none" stroke="#fff" stroke-width="4"/></svg>
    <svg style="left:213px" width="20" height="30" viewBox="0 0 20 30"><polyline points="4,2 16,15 4,28" fill="none" stroke="#fff" stroke-width="4"/></svg>
  </div>
  <div class="abs thumb t1" role="img" aria-label="Photo of guests at the book launch"></div>
  <div class="abs thumb t2" role="img" aria-label="Photo of readers at a table"></div>
  <div class="abs thumb t3" role="img" aria-label="Photo of the launch crowd"></div>
  <p class="abs gallery-text">Neque porro quisquam est qui dolorem ipsum quia dolor sit amet, consectetur, adipisci velit...</p>
  <div class="abs btn" style="left:684px;top:1034px">View More</div>
</section>

<footer class="abs footer">
  <div class="footer-nav">Home<span>|</span>Reviews<span>|</span>About<span>|</span>Blog<span>|</span>Contact<span>|</span>Links</div>
  <div class="copyright">© 2014 Company name , All Rights Reserved</div>
  <div class="social chirp">Chirp</div>
  <div class="social folio">Folio</div>
</footer>
</body>
</html>
```